Book Cover for Willow Kindred Notes from the Meadow

We have written a book that brings together Notes from the Meadow from a variety of women's voices.
We developed a draft book cover that we like using Canva (attached below). We'd love a book cover that is similar to this image, but looks more professional.
Following are the themes we’d like to depict in the book cover, and in parentheses, how they are represented in the current cover:
1. Divinely feminine (overall cover)
2. Currents of enlightenment (the swirls of light carrying the butterfly)
3. Diversity (a myriad of colors)
4. The solo journey into the unknown (the single butterfly’s flight)
5. Buoyancy and joy (again, the dancing colors and floating butterfly)
6. Boldly feminine (the blue butterfly, set against brush strokes of light)
7. Homage to a dear friend (she loved blue butterflies, the cosmos - this butterfly has hints of the cosmos in her wings, and painting - this background has brush strokes of light).
Book Title, Subtitle, and Editor:
Willow Kindred
Notes from the Meadow
Edited by Mirela Tove
Thank you very much for considering this project!
People who are interested in Women and Spirituality

```html
<!DOCTYPE html>
<html lang="en">
<head>
<meta charset="UTF-8">
<title>Willow Kindred — Notes from the Meadow</title>
<link rel="stylesheet" href="https://fonts.googleapis.com/css2?family=Bodoni+Moda:wght@400&family=Great+Vibes&family=Oswald:wght@300&display=swap">
<style>
  :root {
    --page-bg: #e4e4e4;
    --pink: #e3b3d8;
    --violet: #9a7fe0;
    --lilac: #cbbde8;
    --mist: #e6e4ee;
    --teal: #3fbccc;
    --aqua: #8ed3dc;
    --water: #7fc5cf;
    --blush: #ecd3e6;
    --title-white: #f7f6f8;
    --ink: #111114;
    --wing-blue: #32c4ea;
    --wing-deep: #1b8fc4;
  }
  * { margin: 0; padding: 0; box-sizing: border-box; }
  html, body {
    width: 1200px;
    height: 800px;
    overflow: hidden;
    background: var(--page-bg);
  }
  .canvas {
    position: relative;
    width: 1200px;
    height: 800px;
  }
  .book-cover {
    position: absolute;
    left: 364px;
    top: 40px;
    width: 472px;
    height: 720px;
    overflow: hidden;
  }
  .cover-art {
    position: absolute;
    inset: 0;
    background:
      radial-gradient(ellipse 40% 22% at 52% 8%, var(--violet) 0%, rgba(154,127,224,0) 100%),
      radial-gradient(ellipse 45% 35% at 8% 18%, var(--pink) 0%, rgba(227,179,216,0) 100%),
      radial-gradient(ellipse 50% 30% at 90% 12%, var(--mist) 0%, rgba(230,228,238,0) 100%),
      radial-gradient(ellipse 42% 28% at 4% 50%, var(--teal) 0%, rgba(63,188,204,0) 100%),
      radial-gradient(ellipse 50% 30% at 80% 48%, var(--blush) 0%, rgba(236,211,230,0) 100%),
      radial-gradient(ellipse 40% 25% at 10% 72%, var(--lilac) 0%, rgba(203,189,232,0) 100%),
      linear-gradient(180deg, rgba(0,0,0,0) 70%, var(--aqua) 82%, var(--water) 100%),
      linear-gradient(160deg, #dcb8e0 0%, #d9c6ea 40%, #c8dde6 70%, #a9d8de 100%);
  }
  .butterfly-art {
    position: absolute;
    left: 120px;
    top: 330px;
    width: 240px;
    height: 260px;
    border-radius: 50%;
    background:
      radial-gradient(ellipse 45% 38% at 50% 58%, var(--wing-blue) 0%, var(--wing-deep) 45%, rgba(27,143,196,0) 100%),
      radial-gradient(ellipse 50% 50% at 50% 40%, rgba(255,255,255,0.55) 0%, rgba(255,255,255,0) 100%);
  }
  .cover-title {
    position: absolute;
    left: 0;
    right: 0;
    top: 38px;
    text-align: center;
    font-family: "Bodoni Moda", serif;
    font-weight: 400;
    font-size: 88px;
    line-height: 74px;
    letter-spacing: 0.01em;
    color: var(--title-white);
    text-transform: uppercase;
    text-shadow: 1px 2px 3px rgba(80, 60, 110, 0.35);
  }
  .cover-title .title-line { display: block; }
  .cover-subtitle {
    position: absolute;
    left: 0;
    right: 0;
    top: 228px;
    text-align: center;
    font-family: "Great Vibes", cursive;
    font-size: 40px;
    color: var(--ink);
  }
  .editor-credit {
    position: absolute;
    left: 0;
    right: 0;
    top: 632px;
    text-align: center;
    color: var(--ink);
  }
  .editor-label {
    display: block;
    font-family: "Great Vibes", cursive;
    font-size: 22px;
    line-height: 26px;
  }
  .editor-name {
    display: block;
    margin-top: 2px;
    font-family: "Oswald", sans-serif;
    font-weight: 300;
    font-size: 34px;
    letter-spacing: 0.3em;
    padding-left: 0.3em;
    text-transform: uppercase;
  }
</style>
</head>
<body>
<main class="canvas">
  <section class="book-cover">
    <div class="cover-art" role="img" aria-label="Soft painterly brush strokes of pink, violet and turquoise light fading into calm reflective water"></div>
    <div class="butterfly-art" role="img" aria-label="A single bright blue butterfly in flight above the water, surrounded by a trail of sparkling stars"></div>
    <h1 class="cover-title">
      <span class="title-line">Willow</span>
      <span class="title-line">Kindred</span>
    </h1>
    <p class="cover-subtitle">Notes from the Meadow</p>
    <p class="editor-credit">
      <span class="editor-label">Edited by</span>
      <span class="editor-name">Mirela Tove</span>
    </p>
  </section>
</main>
</body>
</html>
```